Create lumora book cover: Paper Lanterns

I need a cover designed for my book
Title is “Paper Lanterns”
Tag line is “ A Ledger of Quiet Seasons“

With the words “ A handbook on how to remove yourself from your company“ somewhere on the page.

Author name “Corin Maddox”

The cover will be used on lumora and paper back and needs to comply with all LPS formatting rules.

Target Market(s)

Small Business owners

Font styles to use
Serif

```html
<!DOCTYPE html>
<html lang="en">
<head>
<meta charset="utf-8">
<title>Paper Lanterns — Corin Maddox</title>
<link rel="stylesheet" href="https://fonts.googleapis.com/css2?family=Playfair+Display:wght@900&family=Libre+Baskerville:wght@700&family=Lora:wght@400&display=swap">
<style>
  :root {
    --paper: #ffffff;
    --floor: #dcdbdc;
    --wood-light: #e9cfa6;
    --wood-mid: #d8b583;
    --wood-edge: #c59c67;
    --title-red: #9b2318;
    --deep-red: #741a12;
    --ink: #111111;
    --tag-ink: #2a1410;
  }
  html, body {
    margin: 0;
    padding: 0;
    width: 750px;
    height: 1200px;
    overflow: hidden;
    background: var(--paper);
  }
  .cover {
    position: relative;
    width: 750px;
    height: 1200px;
    overflow: hidden;
    background: linear-gradient(to bottom, var(--paper) 0%, #f4f4f4 52%, var(--floor) 70%, var(--floor) 100%);
  }
  .cover-art {
    position: absolute;
    inset: 0;
  }
  .author,
  .subtitle {
    position: absolute;
    left: 0;
    width: 750px;
    margin: 0;
    text-align: center;
    font-family: "Lora", serif;
    font-weight: 400;
    color: var(--ink);
  }
  .author {
    top: 112px;
    font-size: 50px;
    line-height: 65px;
    letter-spacing: 1px;
    text-transform: uppercase;
  }
  .subtitle {
    top: 890px;
    font-size: 48px;
    line-height: 67px;
  }
  .title-main,
  .title-second {
    font-family: "Playfair Display", serif;
    font-weight: 900;
    fill: var(--title-red);
  }
  .tagline {
    font-family: "Libre Baskerville", serif;
    font-weight: 700;
  }
  .tagline-top { fill: var(--deep-red); }
  .tagline-mid { fill: var(--tag-ink); }
  .tagline-low { fill: var(--deep-red); }
  .tagline-band { fill: var(--deep-red); }
</style>
</head>
<body>
<main class="cover">
  <svg class="cover-art" width="750" height="1200" viewBox="0 0 750 1200" xmlns="http://www.w3.org/2000/svg">
    <defs>
      <linearGradient id="woodTone" x1="0" y1="0" x2="1" y2="1">
        <stop offset="0" stop-color="var(--wood-light)"/>
        <stop offset="1" stop-color="var(--wood-mid)"/>
      </linearGradient>
    </defs>

    <rect class="photo-blocks" x="140" y="322" width="484" height="478" fill="url(#woodTone)"
          role="img" aria-label="Photograph: a hand placing a stack of three wooden blocks on a white table"/>
    <rect x="140" y="478" width="484" height="3" fill="var(--wood-edge)"/>
    <rect x="140" y="640" width="484" height="3" fill="var(--wood-edge)"/>

    <text class="title-main" x="382" y="462" text-anchor="middle" font-size="160"
          textLength="398" lengthAdjust="spacingAndGlyphs">PAPER</text>
    <text class="title-second" x="382" y="598" text-anchor="middle" font-size="104"
          textLength="398" lengthAdjust="spacingAndGlyphs">LANTERNS</text>

    <rect class="tagline-band" x="197" y="663" width="133" height="27"/>
    <rect class="tagline-band" x="430" y="663" width="133" height="27"/>
    <text class="tagline tagline-top" x="380" y="689" text-anchor="middle" font-size="34">A</text>

    <text class="tagline tagline-mid" x="380" y="735" text-anchor="middle" font-size="32"
          textLength="367" lengthAdjust="spacingAndGlyphs">LEDGER OF QUIET</text>

    <rect class="tagline-band" x="197" y="753" width="80" height="27"/>
    <rect class="tagline-band" x="483" y="753" width="80" height="27"/>
    <text class="tagline tagline-low" x="380" y="779" text-anchor="middle" font-size="32"
          textLength="186" lengthAdjust="spacingAndGlyphs">SEASONS</text>
  </svg>

  <h2 class="author">Corin<br>Maddox</h2>
  <p class="subtitle">A handbook on how to<br>remove yourself from<br>your company</p>
</main>
</body>
</html>
```